Create a channel art for human resources youtube channel

We a are human resource company that want to develop a community on youtube. Our channel is call "PVK Studio" and we will produce videos related to human resources topics like: Strategy, Job Description, selection of workers, workers development, Occupational health, Training, etc.

We need a channel art for our youtube channel that communicate to our viewers what is about the channel.

Attach you can see the logo and icon of the channel, also you can see it here: https://www.vidlumo.example/channel/UCqTbWxe7Rk3LmNpaVhyOdZZ

Target Market(s)

The people who is going to see the art - banner for youtube are persons that work on human resources field

Industry/Entity Type

Business

Font styles to use
Sans Serif

Requirements
Must have
• Must to communicate that our channel is about how to do a better and faster human resources to help business improve there productivity , also workers performances and quality work life. Here are some key words to help you inspire:
• Human Resources
• Performance
• Better
• Faster
• Easier
• Business
• Improve
• Health

```html
<!DOCTYPE html>
<html lang="en">
<head>
<meta charset="UTF-8">
<title>PVK Studio – Channel Banner</title>
<link rel="preconnect" href="https://fonts.googleapis.com">
<link rel="preconnect" href="https://fonts.gstatic.com" crossorigin>
<link href="https://fonts.googleapis.com/css2?family=Arimo:wght@400;700&display=swap" rel="stylesheet">
<style>
  :root {
    --bg-light: #f2f3f5;
    --bg-mid: #dedfe2;
    --bg-cool: #d6dee8;
    --bg-shade: #b9bcc2;
    --tone-warm: #a8978c;
    --tone-deep: #8c8581;
    --text-white: #ffffff;
    --text-shadow: rgba(40, 35, 32, 0.35);
    --badge-fill: rgba(255, 255, 255, 0.85);
    --brand-blue: #29a3dc;
  }

  * { margin: 0; padding: 0; box-sizing: border-box; }

  html, body {
    width: 1200px;
    height: 198px;
    overflow: hidden;
    background: var(--bg-light);
  }

  .banner {
    position: relative;
    width: 1200px;
    height: 198px;
    overflow: hidden;
    font-family: "Arimo", Arial, sans-serif;
  }

  .banner__photo {
    position: absolute;
    inset: 0;
    background:
      radial-gradient(ellipse 230px 85px at 790px 104px, var(--tone-deep), transparent 80%),
      radial-gradient(ellipse 200px 110px at 860px 130px, var(--tone-warm), transparent 75%),
      radial-gradient(ellipse 200px 100px at 290px 110px, var(--bg-mid), transparent 70%),
      radial-gradient(ellipse 60px 80px at 345px 40px, var(--bg-shade), transparent 70%),
      radial-gradient(ellipse 260px 160px at 1060px 80px, var(--bg-cool), transparent 70%),
      linear-gradient(90deg, var(--bg-light) 0%, #e9eaed 40%, #e6e7ea 60%, #e1e6ec 100%);
  }

  .brand-badge {
    position: absolute;
    left: 544px;
    top: 48px;
    width: 100px;
    height: 100px;
    border-radius: 50%;
    background: var(--badge-fill);
    display: flex;
    align-items: center;
    justify-content: center;
  }

  .brand-badge__name {
    font-weight: 700;
    font-size: 16px;
    color: var(--brand-blue);
    white-space: nowrap;
  }

  .headline {
    position: absolute;
    left: 673px;
    top: 72px;
    color: var(--text-white);
    text-shadow: 0 1px 3px var(--text-shadow);
  }

  .headline__title {
    font-size: 29px;
    font-weight: 700;
    line-height: 1;
  }

  .headline__tagline {
    margin-top: 6px;
    font-size: 19px;
    font-weight: 400;
    line-height: 1;
    letter-spacing: 0.4px;
    word-spacing: 6px;
  }
</style>
</head>
<body>
  <div class="banner">
    <div class="banner__photo" role="img" aria-label="Soft-focus office photograph of hands writing in a notebook and holding a tablet"></div>

    <div class="brand-badge">
      <span class="brand-badge__name">PVK Studio</span>
    </div>

    <div class="headline">
      <h1 class="headline__title">Human Resources</h1>
      <p class="headline__tagline">Better Faster Easier</p>
    </div>
  </div>
</body>
</html>
```